Your Joint Helper - Orthopedic needs from one site

We need slides that help to educate users, interest investors and allow the complexity of the entire continuum of care to be explained so anyone can understand. Your Joint Helper is a Varomin Health Company. Yourjointhelperhub.example. We allow people to evaluate, educate and engage with providers from one site. Simplyfying orthopedic care and wellness from one site. Patients, doctors, personal trainers, therapist, nutritionist, yoga, gyms, athletic trainers and more can connect from one site

Target Market(s)

Investors, Patients, Doctors and wellness providers

Industry/Entity Type

Healthcare

Requirements
Must have
• Investor slides, sales slides, education, process....

```html
<!DOCTYPE html>
<html lang="en">
<head>
<meta charset="utf-8">
<title>Your Joint Helper – Orthopedic Problems</title>
<link rel="stylesheet" href="https://fonts.googleapis.com/css2?family=League+Spartan:wght@700&family=Montserrat:wght@500;700&family=Poppins:wght@400&display=swap">
<style>
  :root {
    --paper: #ffffff;
    --leaf: #84c152;
    --ink: #111111;
    --photo-light: #dedede;
    --photo-light-edge: #d2d2d2;
    --photo-dark: #161616;
    --photo-dark-edge: #2a2a2a;
    --brand-ink: #1f2433;
    --brand-dot: #2f9ed8;
  }
  * { margin: 0; padding: 0; box-sizing: border-box; }
  html, body { width: 1200px; height: 900px; overflow: hidden; background: var(--paper); }
  .slide { position: relative; width: 1200px; height: 900px; background: var(--paper); color: var(--ink); }
  .side-band { position: absolute; left: 0; top: 0; width: 232px; height: 900px; background: var(--leaf); }
  .running-head {
    position: absolute; top: 72px;
    font-family: "Montserrat", sans-serif; font-weight: 500;
    font-size: 14px; letter-spacing: 2.4px; text-transform: uppercase;
  }
  .running-head--site { left: 68px; }
  .running-head--page { right: 66px; }
  .photo { position: absolute; }
  .photo--back {
    left: 107px; top: 184px; width: 251px; height: 206px;
    background: linear-gradient(135deg, var(--photo-light), var(--photo-light-edge));
  }
  .photo--elbow {
    left: 370px; top: 90px; width: 293px; height: 197px;
    background: linear-gradient(135deg, var(--photo-light), var(--photo-light-edge));
  }
  .photo--knee {
    left: 107px; top: 465px; width: 379px; height: 344px;
    background: linear-gradient(135deg, var(--photo-dark-edge), var(--photo-dark));
  }
  .title {
    position: absolute; left: 601px; top: 288px;
    font-family: "League Spartan", sans-serif; font-weight: 700;
    font-size: 58px; line-height: 78px; letter-spacing: 4.5px; text-transform: uppercase;
  }
  .problem-list {
    position: absolute; left: 560px; top: 492px; width: 592px;
    font-family: "Poppins", sans-serif; font-size: 26px; line-height: 43.4px;
    list-style: none;
  }
  .problem-list li { position: relative; }
  .problem-list li::before {
    content: ""; position: absolute; left: -26px; top: 18px;
    width: 7px; height: 7px; border-radius: 50%; background: var(--ink);
  }
  .brand {
    position: absolute; right: 38px; top: 785px;
    display: flex; align-items: center; gap: 10px;
    font-family: "Montserrat", sans-serif; font-weight: 700; font-size: 34px; color: var(--brand-ink);
  }
  .brand-dot { width: 22px; height: 22px; border-radius: 50%; background: var(--brand-dot); }
</style>
</head>
<body>
<main class="slide">
  <div class="side-band"></div>
  <p class="running-head running-head--site">Yourjointhelper</p>
  <p class="running-head running-head--page">Page 03</p>

  <div class="photo photo--back" role="img" aria-label="Photo of a man holding his neck and lower back in pain"></div>
  <div class="photo photo--elbow" role="img" aria-label="Photo of a man holding his sore elbow"></div>
  <div class="photo photo--knee" role="img" aria-label="Illustration of a kneeling figure with the knee joint highlighted"></div>

  <h1 class="title">Orthopedic<br>Problems</h1>

  <ul class="problem-list">
    <li>Lower Back Pain. Lower back pain is one of the most common orthopedic issues. …</li>
    <li>Knee pain.</li>
    <li>Hamstring injuries.</li>
    <li>Plantar fasciitis.</li>
    <li>Scoliosis.</li>
    <li>Hip Fracture.</li>
    <li>Arthritis.</li>
  </ul>

  <div class="brand"><span class="brand-dot"></span><span class="brand-name">Varomin</span></div>
</main>
</body>
</html>
```